Small consulting business needs logo and business card design

I need a logo, business card and letterhead design for a small consulting firm called Veltramo Consulting. My customers are generally small to medium sized businesses but I have done work for major corporates and government departments. The field of consulting is strategic/business planning and program management. I have blue as the predominate colour in my current business card but I am happy to change this for the right design
Industry/Entity Type
Business

```html
<!DOCTYPE html>
<html lang="en">
<head>
<meta charset="UTF-8">
<title>Veltramo Consulting – Business Card</title>
<link href="https://fonts.googleapis.com/css2?family=Roboto+Slab:wght@800&family=Open+Sans:wght@400;600&display=swap" rel="stylesheet">
<style>
  :root {
    --page-bg: #e4e4e2;
    --card-dark: #3a3a3c;
    --card-dark-edge: #2e2e30;
    --blue-light: #8fcdf0;
    --blue-mid: #5aa6dc;
    --blue-deep: #3d86c6;
    --silver: #d9dadc;
    --text-light: #ffffff;
    --text-soft: #e8f3fb;
    --logo-colour: #e9eaec;
  }
  * { margin: 0; padding: 0; box-sizing: border-box; }
  html, body {
    width: 1200px; height: 901px; overflow: hidden;
    background: var(--page-bg);
  }
  .stage {
    position: relative; width: 1200px; height: 901px;
  }
  .card {
    position: absolute; top: 118px;
    width: 380px; height: 665px;
    border-radius: 30px; overflow: hidden;
    box-shadow: 0 14px 30px rgba(0,0,0,0.22);
  }
  .card--front { left: 180px; }
  .card--back { left: 640px; background: var(--card-dark); }
  .card-art { position: absolute; inset: 0; width: 100%; height: 100%; }
  .brand {
    position: absolute; left: 0; right: 0;
    font-family: "Roboto Slab", Georgia, serif;
    font-weight: 800; color: var(--logo-colour);
    text-align: center; line-height: 1.05;
  }
  .card--front .brand { top: 62px; }
  .card--back .brand { top: 210px; }
  .brand-line1 { display: block; font-size: 34px; letter-spacing: 1px; text-transform: uppercase; }
  .brand-line2 { display: block; font-size: 38px; }
  .holder {
    position: absolute; left: 46px; top: 330px;
    font-family: "Open Sans", Arial, sans-serif; color: var(--text-light);
  }
  .holder-name { font-size: 25px; font-weight: 600; letter-spacing: 0.5px; text-transform: uppercase; }
  .holder-role { font-size: 17px; color: var(--text-soft); margin-top: 4px; }
  .contacts {
    position: absolute; left: 46px; top: 508px; list-style: none;
    font-family: "Open Sans", Arial, sans-serif; font-size: 19px; color: var(--text-light);
  }
  .contacts li { display: flex; align-items: center; gap: 10px; height: 32px; }
  .contacts svg { width: 18px; height: 18px; flex: none; }
</style>
</head>
<body>
<main class="stage">
  <section class="card card--front">
    <svg class="card-art" viewBox="0 0 380 665" aria-hidden="true">
      <defs>
        <radialGradient id="blueGlow" cx="0.7" cy="0.45" r="0.8">
          <stop offset="0" stop-color="var(--blue-light)"/>
          <stop offset="0.55" stop-color="var(--blue-mid)"/>
          <stop offset="1" stop-color="var(--blue-deep)"/>
        </radialGradient>
      </defs>
      <rect width="380" height="665" fill="var(--card-dark)"/>
      <path d="M0 275 C120 230 260 200 380 205 L380 665 L0 665 Z" fill="url(#blueGlow)"/>
      <path d="M0 230 C110 200 250 178 380 176 L380 184 C250 188 120 208 0 246 Z" fill="var(--silver)"/>
    </svg>
    <div class="brand">
      <span class="brand-line1">Veltramo</span>
      <span class="brand-line2">Consulting</span>
    </div>
    <div class="holder">
      <p class="holder-name">Daniel Marsh</p>
      <p class="holder-role">Managing Director</p>
    </div>
    <ul class="contacts">
      <li>
        <svg viewBox="0 0 24 24" aria-hidden="true"><path fill="#fff" d="M6.6 10.8a15 15 0 0 0 6.6 6.6l2.2-2.2a1 1 0 0 1 1-.25 11.4 11.4 0 0 0 3.6.57 1 1 0 0 1 1 1V20a1 1 0 0 1-1 1A17 17 0 0 1 3 4a1 1 0 0 1 1-1h3.5a1 1 0 0 1 1 1c0 1.25.2 2.45.57 3.6a1 1 0 0 1-.25 1z"/></svg>
        012 555 0148
      </li>
      <li>
        <svg viewBox="0 0 24 24" aria-hidden="true"><rect x="2" y="5" width="20" height="14" rx="1.5" fill="#fff"/><path d="M3 6l9 7 9-7" fill="none" stroke="var(--blue-mid)" stroke-width="1.8"/></svg>
        hello@veltramo.com
      </li>
      <li>
        <svg viewBox="0 0 24 24" aria-hidden="true"><g fill="none" stroke="#fff" stroke-width="1.8"><circle cx="12" cy="12" r="9.5"/><ellipse cx="12" cy="12" rx="4" ry="9.5"/><path d="M2.5 12h19M4 7h16M4 17h16"/></g></svg>
        www.veltramo.com
      </li>
    </ul>
  </section>

  <section class="card card--back">
    <div class="brand">
      <span class="brand-line1">Veltramo</span>
      <span class="brand-line2">Consulting</span>
    </div>
  </section>
</main>
</body>
</html>
```